Holiday Sale 2026 Graphics for New Year

I want to create 10 social media graphics (new Instagram size 4:5 (1080 x 1350 pixels) focusing on our Holiday Sale Graphics, using any of the pics attached. Use the attached pics, NO RANDOM STOCK PHOTOGRAPHY. For the color scheme of the graphics, they should all be complementary to the product colors in the photos.
You can add any of the photos attached but none are required. You can do some of the graphics in all text. I mainly need BOLD text that says one of the headlines with the pics (10 total):
1. 25% OFF Holiday Sale: New You Starts Now!
2. 25% OFF Everything: New Year, New You
3. 25% OFF Christmas Sale 🎁 Feel Amazing Again!
4. Holiday Treat: 25% OFF Your Favorites
5. 25% OFF All Supplements ✨ New Year Reset!
6. Holiday Magic: 25% OFF Every Supplement
7. 25% OFF to Kickstart Your New Year Goals
8. New Year, New Waistline! 25% OFF Sale
9. Holiday Sale: 25% OFF Everything
10. A Better You Begins With 25% OFF

```html
<!DOCTYPE html>
<html lang="en">
<head>
<meta charset="utf-8">
<title>Holiday Sale Graphics Set</title>
<link rel="stylesheet" href="https://fonts.googleapis.com/css2?family=Antonio:wght@600;700&display=swap">
<style>
:root{
  --sheet:#bfc0c2;
  --ink:#2b2b2d;
  --charcoal-top:#1c1c1e;
  --charcoal-mid:#4a4a4c;
  --sale-red:#e3262b;
  --forest:#1f4a3a;
  --forest-light:#3d6f5c;
  --mint:#a8dcca;
  --mint-deep:#5fa98f;
  --navy:#1f2f5c;
  --navy-light:#3a4f86;
  --periwinkle:#b9c4ee;
  --sky-box:#8fb0e6;
  --plum:#8a2a5e;
  --magenta:#c04a92;
  --azure:#2f78c8;
  --wine:#7e1624;
  --wine-light:#b3303f;
  --blush:#f4a3ad;
  --teal-box:#8fd0c0;
  --floor:#e9e6e1;
}
*{margin:0;padding:0;box-sizing:border-box}
html,body{width:1200px;height:612px;overflow:hidden;background:var(--sheet)}
body{position:relative;font-family:"Antonio","Arial Narrow",sans-serif;font-weight:700;text-transform:uppercase}
.tile{position:absolute;width:201px;height:251px;overflow:hidden}
.row-1{top:40px}.row-2{top:320px}
.col-1{left:40px}.col-2{left:270px}.col-3{left:500px}.col-4{left:729px}.col-5{left:959px}
.bg-charcoal{background:linear-gradient(180deg,var(--charcoal-top),var(--charcoal-mid) 60%,#151517)}
.bg-forest{background:radial-gradient(circle at 65% 35%,var(--forest-light),var(--forest) 75%)}
.bg-navy{background:radial-gradient(circle at 65% 35%,var(--navy-light),var(--navy) 75%)}
.bg-white{background:linear-gradient(180deg,#ffffff,#f1f1f1)}
.bg-wine{background:radial-gradient(circle at 65% 35%,var(--wine-light),var(--wine) 75%)}
.floor{position:absolute;left:0;right:0;bottom:0;height:28px;background:var(--floor)}
.photo{position:absolute;border-radius:6px}
.photo-person{background:linear-gradient(180deg,rgba(40,28,24,.55),rgba(235,230,225,.55) 45%,rgba(25,25,30,.7))}
.photo-products{background:linear-gradient(180deg,rgba(255,255,255,.9),rgba(220,220,225,.9))}
.photo-products.on-dark{background:linear-gradient(180deg,rgba(240,240,242,.85),rgba(170,170,175,.85))}
.box{position:absolute;top:0}
.stack{position:absolute;line-height:.98;white-space:nowrap}
.stack span{display:block}
.pct{display:flex;align-items:flex-start;line-height:.85}
.pct .side{display:flex;flex-direction:column;line-height:.9;margin-left:1px}
.center{left:0;right:0;text-align:center}
.center .pct{justify-content:center}
.outline{color:transparent;-webkit-text-stroke:1.5px var(--mint)}
</style>
</head>
<body>

<!-- 1 -->
<section class="tile row-1 col-1 bg-charcoal">
  <div class="box" style="left:32px;width:136px;height:139px;background:var(--sale-red)"></div>
  <div class="stack" style="left:43px;top:12px;color:var(--ink)">
    <span style="font-size:33px">25% OFF</span>
    <span style="font-size:20px">Holiday Sale:</span>
    <span style="font-size:36px">New You</span>
    <span style="font-size:24px">Starts Now!</span>
  </div>
  <div class="photo photo-products on-dark" style="left:6px;top:150px;width:180px;height:96px" role="img" aria-label="Four supplement bottles on a white stone block"></div>
</section>

<!-- 2 -->
<section class="tile row-1 col-2 bg-forest">
  <div class="floor"></div>
  <div class="photo photo-person" style="left:84px;top:34px;width:114px;height:190px" role="img" aria-label="Smiling woman in a white sweater pointing at supplement products"></div>
  <div class="photo photo-products" style="left:54px;top:186px;width:143px;height:60px" role="img" aria-label="Row of supplement bottles and tubes"></div>
  <div class="stack" style="left:9px;top:12px;color:var(--mint)">
    <div class="pct"><span style="font-size:64px">25</span><span class="side"><span style="font-size:36px">%</span><span style="font-size:19px">OFF</span></span></div>
  </div>
  <div class="stack" style="left:10px;top:76px;color:var(--mint-deep)">
    <span style="font-size:19px;color:var(--mint)">Everything:</span>
    <span style="font-size:29px">New</span><span style="font-size:29px">Year</span>
    <span style="font-size:29px">New</span><span style="font-size:29px">You</span>
  </div>
</section>

<!-- 3 -->
<section class="tile row-1 col-3 bg-navy">
  <div class="floor"></div>
  <div class="box" style="left:100px;top:11px;width:101px;height:58px;background:var(--sky-box)"></div>
  <div class="photo photo-person" style="left:86px;top:56px;width:112px;height:170px" role="img" aria-label="Smiling woman in a sheer striped top pointing down at products"></div>
  <div class="stack" style="left:114px;top:15px;color:var(--navy)">
    <span style="font-size:19px">Christmas</span>
    <span style="font-size:23px;display:flex;align-items:center;gap:4px">Sale
      <svg width="16" height="18" viewBox="0 0 18 20" fill="none" stroke="currentColor" stroke-width="2"><rect x="2" y="8" width="14" height="11"/><rect x="1" y="5" width="16" height="4"/><line x1="9" y1="5" x2="9" y2="19"/><path d="M9 5C6 1 3 2 5 5M9 5c3-4 6-3 4 0"/></svg></span>
  </div>
  <div class="stack" style="left:7px;top:12px;color:var(--periwinkle)">
    <div class="pct"><span style="font-size:62px">25</span><span class="side"><span style="font-size:34px">%</span><span style="font-size:18px">OFF</span></span></div>
  </div>
  <div class="stack" style="left:9px;top:80px;color:var(--sky-box)">
    <span style="font-size:48px">Feel</span>
    <span style="font-size:27px">Amazing</span>
    <span style="font-size:32px">Again!</span>
  </div>
</section>

<!-- 4 -->
<section class="tile row-1 col-4 bg-white">
  <div class="stack center" style="top:14px;color:var(--plum)">
    <span style="font-size:21px">Holiday Treat:</span>
    <div class="pct" style="color:var(--magenta)"><span style="font-size:82px">25</span><span class="side"><span style="font-size:46px">%</span><span style="font-size:25px;color:var(--plum)">OFF</span></span></div>
    <span style="font-size:21px">Your Favorites</span>
  </div>
  <div class="photo photo-products" style="left:10px;top:148px;width:183px;height:98px" role="img" aria-label="Four supplement bottles in a row"></div>
</section>

<!-- 5 -->
<section class="tile row-1 col-5 bg-charcoal">
  <div class="box" style="left:35px;width:131px;height:141px;background:var(--sky-box)"></div>
  <div class="stack" style="left:46px;top:12px;color:var(--ink)">
    <span style="font-size:32px">25% OFF</span>
    <span style="font-size:14px">All Supplements ✦</span>
    <span style="font-size:30px">New Year</span>
    <span style="font-size:42px">Reset!</span>
  </div>
  <div class="photo photo-products on-dark" style="left:6px;top:150px;width:180px;height:96px" role="img" aria-label="Four supplement bottles on a white stone block"></div>
</section>

<!-- 6 -->
<section class="tile row-2 col-1 bg-white">
  <div class="stack center" style="top:16px;color:var(--azure)">
    <span style="font-size:22px">Holiday Magic:</span>
    <div class="pct"><span style="font-size:82px">25</span><span class="side"><span style="font-size:46px">%</span><span style="font-size:26px">OFF</span></span></div>
    <span style="font-size:19px">Every Supplement</span>
  </div>
  <div class="photo photo-products" style="left:8px;top:160px;width:186px;height:86px" role="img" aria-label="Four supplement bottles in a row"></div>
</section>

<!-- 7 -->
<section class="tile row-2 col-2 bg-wine">
  <div class="floor"></div>
  <div class="photo photo-person" style="left:92px;top:38px;width:106px;height:190px" role="img" aria-label="Smiling woman in a sheer striped top pointing at supplement bottles"></div>
  <div class="stack" style="left:12px;top:14px;color:var(--blush)">
    <div class="pct"><span style="font-size:60px">25</span><span class="side"><span style="font-size:34px">%</span><span style="font-size:18px">OFF</span></span></div>
  </div>
  <div class="stack" style="left:12px;top:97px;color:var(--blush)">
    <span style="font-size:15px">To Kickstart</span>
    <span style="font-size:34px">Your</span>
    <span style="font-size:19px">New Year</span>
    <span style="font-size:31px">Goals</span>
  </div>
</section>

<!-- 8 -->
<section class="tile row-2 col-3 bg-forest">
  <div class="floor"></div>
  <div class="photo photo-person" style="left:88px;top:56px;width:110px;height:170px" role="img" aria-label="Smiling woman in a white sweater pointing at supplement products"></div>
  <div class="photo photo-products" style="left:58px;top:196px;width:138px;height:51px" role="img" aria-label="Row of supplement bottles and tubes"></div>
  <div class="stack" style="left:10px;top:10px;color:var(--mint)">
    <span style="font-size:30px">New Year,</span>
    <span style="font-size:19px">New Waistline!</span>
  </div>
  <div class="stack outline" style="left:9px;top:72px">
    <div class="pct"><span style="font-size:62px">25</span><span class="side"><span style="font-size:34px">%</span><span style="font-size:18px">OFF</span></span></div>
  </div>
  <div class="stack" style="left:8px;top:142px;color:var(--mint)"><span style="font-size:35px">Sale</span></div>
</section>

<!-- 9 -->
<section class="tile row-2 col-4 bg-charcoal">
  <div class="box" style="left:33px;width:136px;height:121px;background:var(--teal-box)"></div>
  <div class="stack" style="left:42px;top:18px;color:var(--ink)">
    <span style="font-size:22px">Holiday Sale:</span>
    <span style="font-size:34px">25% OFF</span>
    <span style="font-size:26px">Everything</span>
  </div>
  <div class="photo photo-products on-dark" style="left:6px;top:142px;width:180px;height:104px" role="img" aria-label="Four supplement bottles on a white stone block"></div>
</section>

<!-- 10 -->
<section class="tile row-2 col-5 bg-navy">
  <div class="floor"></div>
  <div class="photo photo-person" style="left:102px;top:72px;width:96px;height:158px" role="img" aria-label="Smiling woman in a sheer striped top pointing down at supplement bottles"></div>
  <div class="stack" style="left:29px;top:12px;color:var(--periwinkle)">
    <span style="font-size:30px">A Better You</span>
    <span style="font-size:30px">Begins With</span>
  </div>
  <div class="stack" style="left:27px;top:82px;color:var(--sky-box)">
    <div class="pct"><span style="font-size:62px">25</span><span class="side"><span style="font-size:34px">%</span><span style="font-size:18px">OFF</span></span></div>
  </div>
</section>

</body>
</html>
```